ARC VOLLEY Business Card Project

I'd like to request a business card design for the new company I've launched.
The name of the company is "ARC VOLLEY" an indoor unmanned tennis practice facility.
We would like to see designs that use our brand identity color in the logo I've attached.
We hope to get the design with modern, luxurious and elegant tone and manner.
We hope the logo should not be too big.

Business card must have elements as below:
- Logo (One of the logos I've attached)
- Name (In Korean Text) : 박 서 윤
- Title (In Korean Text) : 대표
- Phone Number : 010-8472-3916
- Email Address : seoyun.park@arcvolley-example.co.kr
- Website : www.arcvolley-example.co.kr
- Instagram : arcvolley
- Address (In Korean text) : 경기도 용인시 수지구 풍덕천로 456 미래타워 5층 501호, 502호

Target Market(s)

Tennis amateurs in 20 to 40s

Industry/Entity Type

Sports, Hobby

Contact Information for Business Card

- Logo (One of the logos I've attached) - Name (In Korean Text) : 박 서 윤 - Title (In Korean Text) : 대표 - Phone Number : 010-8472-3916 - Email Address : seoyun.park@arcvolley-example.co.kr - Website : www.arcvolley-example.co.kr - Instagram : arcvolley - Address (In Korean text) : 경기도 용인시 수지구 풍덕천로 456 미래타워 5층 501호, 502호

Font styles to use
Sans Serif

Requirements
Must have
• Double sided
Nice to have
• Logo with intaglio or relief embossing
Should not have
• Logo should not be too big.

```html
<!DOCTYPE html>
<html lang="ko">
<head>
<meta charset="utf-8">
<title>ARC VOLLEY Business Card</title>
<link rel="stylesheet" href="https://fonts.googleapis.com/css2?family=Noto+Serif+KR:wght@400;600&display=swap">
<style>
  :root {
    --brand-green: #1f4a2c;
    --brand-green-deep: #0b2a14;
    --brand-green-mid: #1c4a2b;
    --emboss-green: #143a20;
    --card-white: #ffffff;
    --card-wash: #f1f2f1;
    --watermark: #e6e8e6;
    --ink: #2a2a2a;
    --rule: #3e6a4a;
    --stage: #e9e7e3;
  }
  * { box-sizing: border-box; margin: 0; padding: 0; }
  html, body { width: 1200px; height: 900px; overflow: hidden; }
  body {
    background: var(--stage);
    font-family: "Noto Serif KR", serif;
    display: flex;
    flex-direction: column;
    align-items: center;
    justify-content: center;
    gap: 22px;
  }
  .card {
    position: relative;
    width: 760px;
    height: 420px;
    border-radius: 0 48px 0 48px;
    overflow: hidden;
    box-shadow: 0 6px 18px rgba(0,0,0,.12);
  }
  /* back side */
  .card-back {
    background: radial-gradient(ellipse at 30% 70%, var(--brand-green-mid) 0%, var(--brand-green-deep) 85%);
    display: flex;
    align-items: center;
    justify-content: center;
  }
  .back-mark {
    display: flex;
    align-items: center;
    gap: 18px;
    color: var(--emboss-green);
  }
  .back-mark .mark-dot {
    width: 64px; height: 64px; border-radius: 50%;
    background: var(--emboss-green);
  }
  .back-mark .mark-name {
    font-size: 46px; font-weight: 600; letter-spacing: 2px;
  }
  /* front side */
  .card-front {
    background: linear-gradient(120deg, var(--card-white) 0%, var(--card-white) 55%, var(--card-wash) 100%);
  }
  .front-watermark {
    position: absolute;
    right: 70px; top: 30px;
    width: 250px; height: 250px;
    border-radius: 50%;
    background: var(--watermark);
  }
  .holder {
    position: absolute; left: 44px; top: 36px;
    color: var(--brand-green);
  }
  .holder-name { font-size: 24px; font-weight: 600; letter-spacing: 4px; }
  .holder-title { font-size: 17px; color: var(--ink); margin-top: 2px; }
  .contacts {
    position: absolute; left: 44px; top: 128px;
    list-style: none;
    font-size: 16px; color: var(--ink); line-height: 1.55;
  }
  .contacts li { display: flex; align-items: flex-start; gap: 10px; }
  .contacts svg { width: 15px; height: 15px; margin-top: 6px; flex: none; fill: var(--brand-green); }
  .rule {
    position: absolute; left: 0; top: 296px;
    width: 520px; height: 1.5px; background: var(--rule);
  }
  .logo-lockup {
    position: absolute; left: 44px; top: 320px;
    display: flex; align-items: center; gap: 14px;
    color: var(--brand-green);
  }
  .logo-lockup .mark-dot {
    width: 62px; height: 62px; border-radius: 50%; background: var(--brand-green);
  }
  .logo-lockup .mark-name { font-size: 38px; font-weight: 600; letter-spacing: 2px; }
  .social {
    position: absolute; right: 44px; top: 244px;
    display: flex; align-items: center; gap: 7px;
    font-size: 16px; color: var(--ink);
  }
  .social .social-dot {
    width: 16px; height: 16px; border-radius: 50%; background: var(--brand-green);
  }
</style>
</head>
<body>

<section class="card card-back" aria-label="Card back">
  <div class="back-mark">
    <span class="mark-dot"></span>
    <span class="mark-name">ARC VOLLEY</span>
  </div>
</section>

<section class="card card-front" aria-label="Card front">
  <div class="front-watermark" aria-hidden="true"></div>

  <div class="holder">
    <p class="holder-name">박 서 윤</p>
    <p class="holder-title">대표</p>
  </div>

  <ul class="contacts">
    <li>
      <svg viewBox="0 0 16 16"><path d="M3 2h3l1 4-2 1a9 9 0 0 0 4 4l1-2 4 1v3a1 1 0 0 1-1 1A13 13 0 0 1 2 3a1 1 0 0 1 1-1z"/></svg>
      <span>010-8472-3916</span>
    </li>
    <li>
      <svg viewBox="0 0 16 16"><path d="M1 4h14v9H1z M1 4l7 5 7-5" fill="none" stroke="#1f4a2c" stroke-width="1.6"/></svg>
      <span>seoyun.park@arcvolley-example.co.kr</span>
    </li>
    <li>
      <svg viewBox="0 0 16 16"><g fill="none" stroke="#1f4a2c" stroke-width="1.4"><circle cx="8" cy="8" r="6.5"/><ellipse cx="8" cy="8" rx="3" ry="6.5"/><path d="M1.5 8h13"/></g></svg>
      <span>www.arcvolley-example.co.kr</span>
    </li>
    <li>
      <svg viewBox="0 0 16 16"><path d="M8 1a5 5 0 0 1 5 5c0 4-5 9-5 9S3 10 3 6a5 5 0 0 1 5-5zm0 3a2 2 0 1 0 0 4 2 2 0 0 0 0-4z"/></svg>
      <span>경기도 용인시 수지구 풍덕천로 456<br>미래타워 5층 501호, 502호</span>
    </li>
  </ul>

  <div class="rule" aria-hidden="true"></div>

  <div class="logo-lockup">
    <span class="mark-dot"></span>
    <span class="mark-name">ARC VOLLEY</span>
  </div>

  <div class="social">
    <span>arcvolley</span>
    <span class="social-dot"></span>
  </div>
</section>

</body>
</html>
```